Event Manager Business Card Design

I am a freelance event manager and work on high end events such as film premieres, product launches and black tie charity dinners. I would like the design to reflect efficiency, reliability, creativity and passion. I am a French Canadian who is now living and working in Sydney, Australia and although I will not be doing any business in Canada, perhaps a Canadian element can be incorporated in the business card to make my card stand out? I would like there to be some white space on the card to allow people to write on it, but not too much. I also want both sides of the card to be used. As a freelancer, I will be handing out my card to anyone with an outstretched hand. It's safe to assume that anyone who gets my card will be receiving hundreds of business cards at a time, so I really need mine to stand out. Please be original! I kind of want people reaction when they receive my card to be "wow, this guy means business, cool card".

Industry/Entity Type

Charity

Contact Information for Business Card

Marc Velline
Event Manager
+61 437 602 915
mvelline4@quorvix.com
brentlo.com/in/marcvelline

Requirements
Should not have
• Cliché event management elements (no film reels, no top hats, etc.)

```html
<!DOCTYPE html>
<html lang="en">
<head>
<meta charset="utf-8">
<title>Marc Velline – Event Manager Business Card Options</title>
<link rel="stylesheet" href="https://fonts.googleapis.com/css2?family=Open+Sans:wght@400;600&family=Roboto+Condensed:wght@700&family=Montserrat:wght@500;600&family=Didact+Gothic&family=Tinos&display=swap">
<style>
  :root {
    --board-light: #2b2b2d;
    --board-dark: #101011;
    --card: #48484b;
    --card-shade: #3b3b3e;
    --leaf: #252325;
    --leaf-front: #39393c;
    --panel: #ffffff;
    --accent: #e3161f;
    --ink: #1e1e1e;
    --contact: #e4e4e4;
    --label: #f2f2f2;
  }
  * { box-sizing: border-box; margin: 0; padding: 0; }
  html, body { width: 1200px; height: 603px; overflow: hidden; }
  body {
    position: relative;
    background: radial-gradient(ellipse at 50% 40%, var(--board-light), var(--board-dark) 85%);
    font-family: "Open Sans", sans-serif;
  }
  .card {
    position: absolute;
    width: 356px;
    height: 204px;
    background: var(--card);
    box-shadow: 0 3px 8px rgba(0,0,0,.7);
    overflow: hidden;
  }
  .card--front { left: 420px; top: 89px; }
  .card--back.opt1 { left: 43px; top: 324px; }
  .card--back.opt2 { left: 421px; top: 324px; }
  .card--back.opt3 { left: 801px; top: 324px; }

  .front-emblem {
    position: absolute;
    left: 124px; top: 50px;
    width: 108px; height: 106px;
    background: var(--leaf-front);
    border-radius: 6px;
  }
  .corner-art { position: absolute; left: 0; top: 0; }
  .corner-emblem {
    position: absolute;
    left: 4px; bottom: 0;
    width: 72px; height: 74px;
    background: var(--leaf);
    border-radius: 4px 4px 0 0;
  }
  .name-panel {
    position: absolute;
    left: 148px; top: 70px;
    width: 208px; height: 64px;
    background: var(--panel);
    border-radius: 6px 0 0 6px;
    padding: 13px 0 0 10px;
    color: var(--ink);
  }
  .name { font-size: 16px; line-height: 20px; white-space: nowrap; }
  .name .first { color: var(--accent); }
  .role { font-size: 10px; line-height: 14px; margin-top: 1px; }

  .opt1 .name { font-family: "Open Sans", sans-serif; font-weight: 400; }
  .opt1 .role { font-family: "Open Sans", sans-serif; }
  .opt2 .name { font-family: "Roboto Condensed", sans-serif; font-weight: 700; font-size: 18px; letter-spacing: 1.5px; }
  .opt2 .role { font-family: "Open Sans", sans-serif; font-weight: 600; }
  .opt3 .name { font-family: "Montserrat", sans-serif; font-weight: 600; letter-spacing: -0.3px; }
  .opt3 .role { font-family: "Montserrat", sans-serif; font-weight: 500; }

  .contact {
    position: absolute;
    right: 16px; top: 141px;
    list-style: none;
    text-align: right;
    font-family: "Didact Gothic", sans-serif;
    font-size: 10px;
    line-height: 16px;
    letter-spacing: 1px;
    color: var(--contact);
  }
  .option-label {
    position: absolute;
    top: 544px;
    width: 356px;
    text-align: center;
    font-family: "Tinos", serif;
    font-size: 22px;
    letter-spacing: 4px;
    color: var(--label);
  }
  .option-label.opt1 { left: 43px; }
  .option-label.opt2 { left: 421px; }
  .option-label.opt3 { left: 801px; }
</style>
</head>
<body>
  <section class="card card--front" aria-label="Card front">
    <div class="front-emblem" role="img" aria-label="Maple leaf emblem, tone on tone"></div>
  </section>

  <section class="card card--back opt1" aria-label="Card back, option 01">
    <svg class="corner-art" width="356" height="204" viewBox="0 0 356 204" aria-hidden="true">
      <path d="M0,118 Q10,118 22,132 L72,186 Q86,204 112,204 L0,204 Z" fill="var(--card-shade)"/>
    </svg>
    <div class="corner-emblem" role="img" aria-label="Maple leaf emblem"></div>
    <div class="name-panel">
      <p class="name"><span class="first">MARC</span> VELLINE</p>
      <p class="role">Event Manager</p>
    </div>
    <ul class="contact">
      <li>+61 437 602 915</li>
      <li>mvelline4@quorvix.com</li>
      <li>brentlo.com/in/marcvelline</li>
    </ul>
  </section>

  <section class="card card--back opt2" aria-label="Card back, option 02">
    <svg class="corner-art" width="356" height="204" viewBox="0 0 356 204" aria-hidden="true">
      <path d="M0,118 Q10,118 22,132 L72,186 Q86,204 112,204 L0,204 Z" fill="var(--card-shade)"/>
    </svg>
    <div class="corner-emblem" role="img" aria-label="Maple leaf emblem"></div>
    <div class="name-panel">
      <p class="name"><span class="first">MARC</span> VELLINE</p>
      <p class="role">Event Manager</p>
    </div>
    <ul class="contact">
      <li>+61 437 602 915</li>
      <li>mvelline4@quorvix.com</li>
      <li>brentlo.com/in/marcvelline</li>
    </ul>
  </section>

  <section class="card card--back opt3" aria-label="Card back, option 03">
    <svg class="corner-art" width="356" height="204" viewBox="0 0 356 204" aria-hidden="true">
      <path d="M0,118 Q10,118 22,132 L72,186 Q86,204 112,204 L0,204 Z" fill="var(--card-shade)"/>
    </svg>
    <div class="corner-emblem" role="img" aria-label="Maple leaf emblem"></div>
    <div class="name-panel">
      <p class="name"><span class="first">MARC</span> VELLINE</p>
      <p class="role">Event Manager</p>
    </div>
    <ul class="contact">
      <li>+61 437 602 915</li>
      <li>mvelline4@quorvix.com</li>
      <li>brentlo.com/in/marcvelline</li>
    </ul>
  </section>

  <p class="option-label opt1">OPTION 01</p>
  <p class="option-label opt2">OPTION 02</p>
  <p class="option-label opt3">OPTION 03</p>
</body>
</html>
```